Stylish Business Card for Modern hair salon

I need a simple business card design using our salon logo and colours that are in the logo. We service clients of all ages but predominantly those in the 18 to 55 age range. We have a young staff and are looking to have a card that will present a modern and clean image that represents who we are. The card should be in black and white same as our logo. Minimal use of other colours is allowed.

Industry/Entity Type

Hair And Beauty

Contact Information for Business Card

The design should have the following information
salon name - TR Hair Studio
address - 2751 Birchfield Rd.E. Mississauga, ON L7P3K2
phone - 905 614-2870
website - trhairexample.ca
instagram - tr.hairstudio
twitter - @TR_HairStudio

Colors
000000
ffffff
474747

Requirements
Must have
• simple design, salon name, address, phone, website, instagram, twitter info
• Back of card should have the following:
• YOUR NEXT APPOINTMENT
• DATE
• TIME
Nice to have
• simple design, clear to see and read,
• predominantly black and white colour, minimal use of other colours is ok
Should not have
• many colours, various fonts

```html
<!DOCTYPE html>
<html lang="en">
<head>
<meta charset="utf-8">
<title>TR Hair Studio — Business Card</title>
<link rel="stylesheet" href="https://fonts.googleapis.com/css2?family=Lato:wght@400;700&display=swap">
<style>
  :root {
    --ink: #000000;
    --paper: #ffffff;
    --grey: #474747;
    --stage: #2e2e2e;
    --card-dark: #1c1c1c;
    --muted: #8a8a8a;
  }
  * { box-sizing: border-box; margin: 0; padding: 0; }
  html, body {
    width: 1200px; height: 716px; overflow: hidden;
    background: var(--stage);
    font-family: "Lato", Arial, sans-serif;
  }
  .stage {
    position: relative; width: 1200px; height: 716px;
    display: flex; align-items: center; justify-content: center; gap: 40px;
  }
  .card {
    position: relative; width: 520px; height: 298px;
    border-radius: 18px; overflow: hidden;
  }
  .card--front { background: var(--paper); color: var(--ink); }
  .card--back { background: var(--card-dark); color: var(--paper); }

  .brand-name {
    position: absolute; left: 0; right: 0; top: 48px;
    text-align: center; font-size: 40px; font-weight: 700;
    letter-spacing: 1px;
  }
  .card--front .brand-name { color: var(--ink); }
  .card--back .brand-name { color: var(--paper); top: 36px; }

  .appointment {
    position: absolute; left: 0; right: 0; top: 140px; text-align: center;
  }
  .appointment__title { font-size: 17px; margin-bottom: 26px; }
  .appointment__fields {
    display: flex; justify-content: center; gap: 34px; font-size: 16px;
  }
  .field { display: flex; align-items: flex-end; }
  .field__line {
    display: inline-block; width: 120px; border-bottom: 1.5px solid var(--ink);
    margin-left: 4px; height: 18px;
  }

  .contact-list {
    position: absolute; left: 44px; top: 118px; list-style: none;
    font-size: 15px; line-height: 1;
  }
  .contact-list li {
    display: flex; align-items: center; gap: 12px; margin-bottom: 12px;
  }
  .contact-icon { width: 14px; height: 14px; flex: none; }
  .contact-icon--plain {
    width: 12px; height: 12px; background: var(--paper); border-radius: 2px; margin: 0 1px;
  }
  .website {
    position: absolute; right: 26px; bottom: 20px; font-size: 13px; color: var(--muted);
  }
</style>
</head>
<body>
<main class="stage">
  <section class="card card--front" aria-label="Front of card: next appointment">
    <div class="brand-name">TR Hair Studio</div>
    <div class="appointment">
      <p class="appointment__title">Your Next Appointment:</p>
      <div class="appointment__fields">
        <span class="field">Date:<span class="field__line"></span></span>
        <span class="field">Time:<span class="field__line"></span></span>
      </div>
    </div>
  </section>

  <section class="card card--back" aria-label="Back of card: contact details">
    <div class="brand-name">TR Hair Studio</div>
    <ul class="contact-list">
      <li>
        <svg class="contact-icon" viewBox="0 0 14 14" aria-hidden="true">
          <path d="M7 1a4 4 0 0 0-4 4c0 3 4 8 4 8s4-5 4-8a4 4 0 0 0-4-4z" fill="none" stroke="#fff" stroke-width="1.5"/>
          <circle cx="7" cy="5" r="1.4" fill="#fff"/>
        </svg>
        2751 Birchfield Rd.E. Mississauga, ON L7P3K2
      </li>
      <li>
        <svg class="contact-icon" viewBox="0 0 14 14" aria-hidden="true">
          <path d="M3 1.5l2.2 2.6-1.2 1.6a8 8 0 0 0 4.3 4.3l1.6-1.2 2.6 2.2-1.3 1.8C6 12.5 1.5 8 1.2 2.8z" fill="#fff"/>
        </svg>
        905 614-2870
      </li>
      <li><span class="contact-icon contact-icon--plain"></span>tr.hairstudio</li>
      <li><span class="contact-icon contact-icon--plain"></span>@TR_HairStudio</li>
    </ul>
    <div class="website">trhairexample.ca</div>
  </section>
</main>
</body>
</html>
```